Business Card and Letterhead for Vantage Psychology

We need a business card design and letterhead to use for our Psychology firm that specializes in psychoeducational assessments and individual therapy. Our motto is Purpose-Driven Assessments, Meaning-Centered Therapy.Our contact information is as follows:
Vantage Psychology
The Marwick Block - 6127-48St.
Box 2716 Larkfield, AB
T2K 3M8
t 403.555.0148 (VANT)
f 403.555.0172
www.vantagepsychology-example.ca
The business card will be used for two different psychologists so I can supply names nearer to completion. We prefer clean, uncluttered looks.

Target Market(s)

Clients, Educators

Font styles to use
Sans Serif

Colors

Designer to choose colors to be used in the design.

Requirements
Must have
• All relevant contact info, logo, some "white" space.
Nice to have
• It would be nice to see letterhead options that have the logo on the top of the page but also options that have it on the side. I think top of the page is probably our preference.
Should not have
• Too much clutter!

```html
<!DOCTYPE html>
<html lang="en">
<head>
<meta charset="utf-8">
<title>Vantage Psychology – Letterhead and Business Card</title>
<link rel="stylesheet" href="https://fonts.googleapis.com/css2?family=Lato:ital,wght@0,400;0,700;1,400;1,700&family=Michroma&family=Pinyon+Script&display=swap">
<style>
:root{
  --blue:#3fa3c2;
  --blue-light:#55b3cf;
  --orange:#e2873e;
  --ink:#3d3d3d;
  --grey-text:#555;
  --paper:#f7f7f8;
  --bg:#e4e4e4;
}
*{box-sizing:border-box;margin:0;padding:0}
html,body{width:1001px;height:1200px;overflow:hidden;background:var(--bg);font-family:'Lato',sans-serif}
.canvas{position:relative;width:1001px;height:1200px}

/* Letterhead */
.letterhead{position:absolute;left:313px;top:137px;width:359px;height:513px;background:var(--paper);overflow:hidden}
.brand{position:absolute;left:26px;top:20px;width:92px;text-align:center}
.brand-mark{display:block;width:24px;height:24px;border-radius:50%;background:var(--blue);margin:0 auto 4px}
.brand-name{font-size:7.2px;font-weight:700;color:var(--blue);letter-spacing:.3px;white-space:nowrap}
.divider{position:absolute;top:34px;width:1px;height:22px;background:var(--blue)}
.divider.one{left:125px}.divider.two{left:233px}
.head-address,.head-contact{position:absolute;top:35px;font-size:5.6px;line-height:7.5px;color:var(--grey-text);white-space:nowrap}
.head-address{left:138px}
.head-contact{left:245px}
.head-address .postcode{color:var(--orange)}
.head-contact .ic{display:inline-block;width:4px;height:4px;border-radius:50%;background:var(--orange);margin-right:3px;vertical-align:middle}
.letter{position:absolute;left:47px;top:115px;width:265px;font-size:5.6px;line-height:8.6px;color:var(--ink)}
.letter .date{margin-bottom:9px}
.letter .recipient{margin-bottom:17px}
.letter .recipient strong{font-weight:700;color:#111}
.letter .salutation{margin-bottom:8px}
.letter p.body{text-align:justify;margin-bottom:8px}
.letter .closing{margin-top:22px}
.letter .signature{font-family:'Pinyon Script',cursive;font-size:11.5px;line-height:16px;margin-left:3px;color:#111}
.letter-footer{position:absolute;left:0;bottom:0;width:359px;height:75px}
.footer-tagline{position:absolute;right:15px;bottom:10px;text-align:right;font-size:5.6px;line-height:7.4px;font-style:italic;font-weight:700;color:#fff}

/* Business card front */
.card{position:absolute;top:858px;width:318px;height:177px;border-radius:14px;overflow:hidden}
.card-front{left:149px;background:linear-gradient(160deg,#f5f5f5,#e6e6e6)}
.card-front svg{position:absolute;inset:0}
.card-front .brand{left:28px;top:22px;width:94px}
.card-front .brand-mark{width:28px;height:28px}
.card-front .brand-name{font-size:7.6px}
.person{position:absolute;left:26px;top:92px}
.person-name{font-family:'Michroma',sans-serif;font-size:8.4px;color:var(--orange);letter-spacing:.3px}
.person-role{font-size:7px;color:var(--blue)}
.card-contact,.card-address{position:absolute;right:20px;text-align:right;color:#fff;font-size:6.8px;line-height:9.5px;white-space:nowrap}
.card-contact{top:103px}
.card-address{top:140px}
.card-contact .ic{display:inline-block;width:4.5px;height:4.5px;border-radius:50%;background:#fff;margin-left:4px;vertical-align:middle}
.card-address strong{font-weight:700}

/* Business card back */
.card-back{left:519px;background:var(--blue-light)}
.back-mark{position:absolute;left:50%;top:28px;width:52px;height:52px;margin-left:-26px;border-radius:50%;background:#f0f4f5}
.back-name{position:absolute;left:0;right:0;top:119px;text-align:center;font-size:13px;font-weight:700;color:#f0f4f5;letter-spacing:.6px}
.back-tagline{position:absolute;left:0;right:0;top:154px;text-align:center;font-size:6.8px;font-style:italic;color:#f0f4f5}
</style>
</head>
<body>
<main class="canvas">

  <section class="letterhead" aria-label="Letterhead">
    <header>
      <div class="brand"><span class="brand-mark"></span><span class="brand-name">Vantage Psychology</span></div>
      <span class="divider one"></span>
      <div class="head-address">Vantage Psychology<br>The Marwick Block - 6127-48St.<br>Box 2716 Larkfield, AB | <span class="postcode">T2K 3M8</span></div>
      <span class="divider two"></span>
      <div class="head-contact"><span class="ic"></span>403.555.0148 (VANT)<br><span class="ic"></span>403.555.0172<br><span class="ic"></span>www.vantagepsychology-example.ca</div>
    </header>

    <article class="letter">
      <p class="date">01 January 2050</p>
      <p class="recipient"><strong>Company (Pvt) Ltd.</strong><br>PO Box 4410 Elmford St<br>Sample City Country 4410</p>
      <p class="salutation">Dear Laura Whitcombe,</p>
      <p class="body">Lorem ipsum dolor sit amet, consectetuer adipiscing elit, sed diam nonummy nibh euismod tincidunt ut laoreet dolore magna aliquam erat volutpat. Ut wisi enim ad minim veniam, quis nostrud exerci tation ullamcorper suscipit lobortis nisl ut aliquip ex ea commodo consequat. Duis dolore te feugait nulla facilisi. Nam liber tempor cum soluta nobis eleifend option congue nihil imperdiet doming id quod mazim placerat facer possim assum. Lorem ipsum dolor sit amet, consectetuer adipiscing elit, sed diam nonummy nibh euismod tincidunt ut laoreet dolore magna aliquam erat volutpat. Ut wisi enim ad minim veniam, quis nostrud exerci tation ullamcorper suscipit lobortis nisl ut aliquip ex ea commodo consequat.</p>
      <p class="body">Consectetuer adipiscing elit, sed diam nonummy nibh euismod tincidunt ut laoreet dolore magna aliquam erat volutpat. Ut wisi enim ad minim veniam, quis nostrud exerci tation ullamcorper suscipit lobortis nisl ut aliquip ex ea commodo consequat. Consectetuer adipiscing elit, sed diam nonummy nibh euismod tincidunt ut laoreet dolore magna aliquam erat volutpat. Ut wisi enim ad minim veniam, quis nostrud exerci tation ullamcorper suscipit lobortis nisl ut aliquip ex ea commodo consequat.</p>
      <p class="body">Consectetuer adipiscing elit, sed diam nonummy nibh euismod tincidunt ut laoreet dolore magna aliquam erat volutpat. Ut wisi enim ad minim veniam, quis nostrud exerci tation ullamcorper suscipit lobortis nisl ut aliquip ex ea commodo consequat. Consectetuer adipiscing elit, sed diam nonummy nibh euismod tincidunt ut laoreet dolore magna aliquam erat volutpat. Ut wisi enim ad minim veniam, quis nostrud exerci tation ullamcorper suscipit lobortis nisl ut aliquip ex ea commodo consequat.</p>
      <p class="closing">Sincerely Yours</p>
      <p class="signature">Graham Alden Pryce</p>
    </article>

    <footer>
      <svg class="letter-footer" viewBox="0 0 359 75" preserveAspectRatio="none" aria-hidden="true">
        <path d="M0 32 Q150 62 359 0 L359 75 L0 75 Z" fill="var(--blue)"/>
        <path d="M0 42 Q150 70 290 34 Q150 62 0 32 Z" fill="var(--orange)"/>
        <path d="M0 42 Q150 72 290 34 Q150 68 0 45 Z" fill="#fff"/>
      </svg>
      <p class="footer-tagline">Thoughtful Assessments,<br>Person-Centered Care.</p>
    </footer>
  </section>

  <section class="card card-front" aria-label="Business card front">
    <svg viewBox="0 0 318 177" preserveAspectRatio="none" aria-hidden="true">
      <path d="M0 140 Q200 130 318 0 L318 177 L0 177 Z" fill="var(--blue-light)"/>
      <path d="M0 124 Q150 128 250 60 Q160 120 0 137 Z" fill="var(--orange)"/>
      <path d="M0 137 Q160 120 250 60 Q170 126 0 141 Z" fill="#fff"/>
    </svg>
    <div class="brand"><span class="brand-mark"></span><span class="brand-name">Vantage Psychology</span></div>
    <div class="person">
      <p class="person-name">DANIEL OKAFOR</p>
      <p class="person-role">Psychologists</p>
    </div>
    <p class="card-contact">(Vant) 403.555.0148<span class="ic"></span><br>403.555.0172<span class="ic"></span><br>www.vantagepsychology-example.ca<span class="ic"></span></p>
    <p class="card-address">Vantage Psychology<br>The Marwick Block - 6127-48St.<br>Box 2716 Larkfield, AB | <strong>T2K 3M8</strong></p>
  </section>

  <section class="card card-back" aria-label="Business card back">
    <span class="back-mark"></span>
    <p class="back-name">VANTAGE PSYCHOLOGY</p>
    <p class="back-tagline">Thoughtful Assessments, Person-Centered Care.</p>
  </section>

</main>
</body>
</html>
```